Harbor LunaVital & Equipments

I need to create full stationery design for the company; Business Card, Envelop, Letterheads, Calendar and email template.

Our company is specialized in the import and export of nutritional, pharmaceutical and cosmetics in addition to medical equipments.

These is no limitation on how to use colors within the design.

Target Market(s)

Global

Industry/Entity Type

Healthcare

Other font styles liked:
• a font close to logo. Letterhead body text to be different than the address text

Requirements
Nice to have
• We will have multiple locations so it is good to keep space for future addresses.
• Stationary requirements:
• Letterhead: A4
• Envelopes: 3 regular sizes : large, medium and small (i do not know the sizes)
• Colors: extracted from the logo

```html
<!DOCTYPE html>
<html lang="en">
<head>
<meta charset="utf-8">
<title>Harbor LunaVital &amp; Equipments – Business Card</title>
<link href="https://fonts.googleapis.com/css2?family=Arimo:ital,wght@0,400;0,700;1,400&display=swap" rel="stylesheet">
<style>
  :root {
    --page-bg: #e4e5ea;
    --card-bg: #fbfbfd;
    --brand-blue: #1f7fc4;
    --brand-green: #2c9a35;
    --ink-dark: #1e2030;
    --band-navy: #191a45;
    --band-navy-light: #2c3174;
    --band-text: #e7e8f3;
    --band-muted: #b9bbd6;
  }
  * { box-sizing: border-box; margin: 0; padding: 0; }
  html, body {
    width: 1200px; height: 969px; overflow: hidden;
    background: var(--page-bg);
    font-family: "Arimo", Arial, sans-serif;
  }
  .canvas { position: relative; width: 1200px; height: 969px; }
  .business-card {
    position: absolute; left: 100px; top: 201px;
    width: 1000px; height: 567px;
    background: var(--card-bg);
    border-radius: 22px;
    overflow: hidden;
    box-shadow: 0 18px 40px rgba(20, 22, 50, 0.18);
  }
  .brand {
    position: absolute; left: 55px; top: 48px;
  }
  .brand-mark {
    display: block; width: 62px; height: 62px;
    background: var(--brand-blue);
    border-radius: 6px;
    margin: 0 0 16px 70px;
  }
  .brand-name {
    color: var(--brand-blue);
    font-weight: 700;
    font-size: 40px;
    line-height: 1.1;
    letter-spacing: -0.5px;
  }
  .contact-person {
    position: absolute; right: 58px; top: 82px;
    text-align: right;
  }
  .person-name { color: var(--brand-blue); font-size: 31px; line-height: 1.2; }
  .person-title { color: var(--brand-green); font-size: 27px; line-height: 1.25; }
  .person-email { color: var(--ink-dark); font-size: 26px; font-style: italic; line-height: 1.3; }
  .info-band {
    position: absolute; left: 0; right: 0; top: 280px; bottom: 0;
    background: linear-gradient(100deg, var(--band-navy) 0%, var(--band-navy-light) 55%, var(--band-navy) 100%);
  }
  .address {
    position: absolute; left: 55px; top: 30px;
    color: var(--band-text); font-size: 25px; line-height: 1.4;
  }
  .contact-lines {
    position: absolute; left: 55px; top: 120px;
    list-style: none;
    color: var(--band-text); font-size: 25px;
  }
  .contact-lines li { display: flex; align-items: center; gap: 12px; height: 38px; }
  .contact-lines li.web { color: var(--band-muted); }
  .contact-lines svg { width: 24px; height: 24px; fill: var(--band-text); flex: none; }
  .contact-lines li.web svg { fill: var(--band-muted); }
</style>
</head>
<body>
<main class="canvas">
  <article class="business-card">
    <header class="brand">
      <span class="brand-mark"></span>
      <p class="brand-name">Harbor LunaVital<br>&amp; Equipments</p>
    </header>

    <section class="contact-person">
      <p class="person-name">Mara Quill</p>
      <p class="person-title">President</p>
      <p class="person-email">mara@harborluna.com</p>
    </section>

    <section class="info-band">
      <address class="address" style="font-style: normal;">
        1420 Willow Crest Road<br>
        Juneau, Alaska 34818
      </address>
      <ul class="contact-lines">
        <li class="phone">
          <svg viewBox="0 0 24 24" aria-hidden="true"><path d="M3 8c0-2 2-4 9-4s9 2 9 4v2h-5V8H8v2H3z"/><path d="M6 12h12l2 8H4z"/></svg>
          512 3906 7741
        </li>
        <li class="fax">
          <svg viewBox="0 0 24 24" aria-hidden="true"><path d="M7 3h10v5H7z"/><path d="M3 9h18v8h-3v-3H6v3H3z"/><path d="M7 15h10v6H7z"/></svg>
          512 3906 7742
        </li>
        <li class="web">
          <svg viewBox="0 0 24 24" aria-hidden="true"><path d="M12 2a10 10 0 1 0 0 20 10 10 0 0 0 0-20zm0 2c1.4 0 2.8 2.6 3.2 7H8.8C9.2 6.6 10.6 4 12 4zM4.1 13h2.7c.1 1.8.4 3.5 1 4.8A8 8 0 0 1 4.1 13zm0-2a8 8 0 0 1 3.7-4.8c-.6 1.3-.9 3-1 4.8zm7.9 9c-1.4 0-2.8-2.6-3.2-7h6.4c-.4 4.4-1.8 7-3.2 7zm4.2-2.2c.6-1.3.9-3 1-4.8h2.7a8 8 0 0 1-3.7 4.8zm1-6.8c-.1-1.8-.4-3.5-1-4.8a8 8 0 0 1 3.7 4.8z"/></svg>
          www.harborluna.com
        </li>
      </ul>
    </section>
  </article>
</main>
</body>
</html>
```